Sudsy Harbor Laundromat Wordpress Design

We need a Wordpress website design for our laundromat, Sudsy Harbor Atlanta, at www.sudsyharborlaunder.example. We would like to have 6 pages: Home, About Us, Services, Locations, Reviews and Contact us. We will provide content for the text on each page. What we do: We are a full service laundromat that provides dry cleaning drop off, professional laundry services, wash dry fold and self service laundry to the local community. We would like to use the color scheme from our logo to convey a warm, safe, and bright business that caters to its diverse community.
Updates

I like the structure of this laundromat website: http://www.tumblewashexample.com/ Using my logo and color scheme in the above referenced website is what. Am looking for. The photos attached to the project with the female model should be used as a primary focus and supplemented by actual photos of the equipment.

Target Market(s)

Our target market is a diverse group of people from Midtown Atlanta - LGBTQ community /Locals/Regulars that have been coming to laundromat for 30 years.

Industry/Entity Type

Laundromat

Coding

Coded - Design and coding required

Number of Pages Required

5+ page

Font styles to use
Sans Serif

Colors
0054AA
0677BA
7BADD7
CADEEF
E8F1F8

Requirements
Must have
• Feature this video on the main page: https://videos.example.net/wq7PzrT2kLm

```html
<!DOCTYPE html>
<html lang="en">
<head>
<meta charset="utf-8">
<title>Sudsy Harbor Laundromat</title>
<link rel="stylesheet" href="https://fonts.googleapis.com/css2?family=Open+Sans:ital,wght@0,400;0,600;0,700;0,800;1,400&display=swap">
<style>
:root{
  --navy:#0054AA;
  --blue:#0677BA;
  --sky:#1E9BD7;
  --soft:#7BADD7;
  --pale:#CADEEF;
  --mist:#E8F1F8;
  --ink:#333333;
  --muted:#555555;
  --white:#ffffff;
  --footer:#111111;
  --star:#F5B700;
}
*{box-sizing:border-box;margin:0;padding:0}
html,body{width:1200px;height:4170px;overflow:hidden}
body{font-family:"Open Sans",sans-serif;color:var(--ink);background:var(--white);position:relative}
section,header,footer{position:absolute;left:0;width:1200px}
.abs{position:absolute}

/* header */
.site-header{top:0;height:107px;background:var(--white)}
.brand{left:110px;top:40px;font-size:16px;font-weight:700;color:var(--navy);display:flex;align-items:center;gap:8px;white-space:nowrap}
.brand-dot{width:14px;height:14px;border-radius:50%;background:var(--sky);flex:none}
.nav{left:393px;top:49px;display:flex;gap:24px;font-size:13px;font-weight:600;color:var(--navy);text-transform:uppercase;white-space:nowrap}
.call{left:957px;top:0;width:243px;height:107px;background:var(--navy);color:var(--white)}
.call-icon{left:-24px;top:28px;width:50px;height:50px;border-radius:50%;background:var(--sky);display:flex;align-items:center;justify-content:center;border:3px solid var(--white)}
.call-label{left:42px;top:34px;font-size:13px;font-weight:600}
.call-num{left:42px;top:50px;font-size:21px;font-weight:700;white-space:nowrap}

/* hero */
.hero{top:107px;height:709px}
.hero-photo{position:absolute;inset:0;background:linear-gradient(180deg,#6b8fa8 0%,#4d6b80 45%,#8a9aa5 100%)}
.hero-title{left:110px;top:218px;font-size:53px;line-height:51px;font-weight:800;color:var(--white);text-transform:uppercase}
.btn-ghost{left:110px;top:440px;width:152px;height:46px;border:2px solid var(--sky);border-radius:24px;color:var(--white);font-size:13px;font-weight:700;display:flex;align-items:center;justify-content:center}
.dots{left:110px;top:590px;display:flex;gap:8px}
.dots span{width:11px;height:11px;border-radius:50%;background:var(--white)}
.social-side{left:1124px;top:292px;display:flex;flex-direction:column;gap:17px}
.social-side span{width:31px;height:31px;border-radius:50%;border:2px solid var(--white)}

/* about */
.about{top:816px;height:671px}
.about-photo-back{left:110px;top:102px;width:490px;height:246px;background:linear-gradient(135deg,#0d5a7d,#1a7fa3)}
.about-photo-front{left:186px;top:225px;width:340px;height:341px;background:linear-gradient(160deg,#c9c5bd,#8f8d88 60%,#5a6f96)}
.bubble{border-radius:50%;border:4px solid var(--navy);background:var(--white)}
.eyebrow{left:655px;top:100px;font-size:14px;font-weight:700;letter-spacing:4px;color:var(--blue)}
.about-title{left:650px;top:130px;font-size:38px;font-weight:600;color:var(--ink)}
.about-text{left:651px;top:187px;width:433px;font-size:14px;line-height:21.5px;color:var(--muted)}
.btn-outline{border:3px solid var(--navy);border-radius:28px;color:var(--navy);font-weight:700;font-size:14px;display:flex;align-items:center;justify-content:center}

/* services */
.services{top:1487px;height:671px;background:var(--mist)}
.section-title{left:0;width:1200px;text-align:center;font-size:38px;font-weight:700;color:var(--ink)}
.card{top:173px;width:313px;height:394px;background:var(--white);box-shadow:0 4px 14px rgba(0,40,90,.08)}
.card-photo{position:absolute;left:0;top:0;width:313px;height:205px}
.card-icon{position:absolute;left:121px;top:160px;width:72px;height:72px;border-radius:50%;background:var(--white);border:2px solid var(--pale);display:flex;align-items:center;justify-content:center}
.card-title{position:absolute;left:0;top:248px;width:313px;text-align:center;font-size:22px;font-weight:600;line-height:30px}
.btn-solid{position:absolute;left:78px;top:320px;width:158px;height:40px;border-radius:22px;background:var(--navy);color:var(--white);font-size:13px;font-weight:700;display:flex;align-items:center;justify-content:center;gap:5px}

/* video */
.video{top:2158px;height:680px}
.video-title{top:90px;color:var(--white)}
.video-sub{left:290px;top:155px;width:620px;text-align:center;font-size:14px;line-height:21px;color:var(--white)}
.video-frame{left:232px;top:228px;width:735px;height:384px;background:linear-gradient(135deg,#5c5a52,#2f2e2b 60%,#4a4840)}
.play{left:325px;top:150px;width:85px;height:85px;border-radius:50%;background:var(--white);border:6px solid var(--sky);display:flex;align-items:center;justify-content:center}

/* reviews */
.reviews{top:2838px;height:488px}
.review{top:107px;width:316px;height:201px;border:2px solid var(--blue);padding:24px 30px}
.stars{color:var(--star);font-size:14px;letter-spacing:2px}
.quote{margin-top:12px;font-size:13px;line-height:21px;font-style:italic;color:var(--muted)}
.tail{position:absolute;left:34px;bottom:-26px}
.reviewer{top:350px;font-size:17px;font-weight:700}
.company{top:376px;font-size:12px;color:var(--muted)}

/* contact */
.contact{top:3326px;height:462px}
.map{left:0;top:0;width:601px;height:462px;background:linear-gradient(135deg,#e9ede8,#dfe6e0 50%,#e4e9ef)}
.contact-panel{left:601px;top:0;width:599px;height:462px;background:linear-gradient(135deg,var(--navy),var(--sky))}
.contact-title{left:77px;top:55px;font-size:38px;font-weight:700;color:var(--white)}
.c-icon{left:77px;width:48px;height:48px;border-radius:50%;background:var(--white);display:flex;align-items:center;justify-content:center}
.c-text{left:159px;width:260px;font-size:13px;font-weight:700;line-height:26px;color:var(--white)}
.ring{border-radius:50%;border:4px solid var(--navy);opacity:.8}

/* footer */
.site-footer{top:3788px;height:382px;background:var(--footer);color:var(--white)}
.f-head{top:68px;font-size:15px;font-weight:700}
.f-line{height:2px;width:62px;background:var(--white)}
.f-row{left:113px;display:flex;gap:16px;font-size:13px;line-height:21px}
.f-ico{width:28px;height:28px;border-radius:50%;border:2px solid var(--white);flex:none;display:flex;align-items:center;justify-content:center}
.f-links{left:465px;top:117px;list-style:none;font-size:13px;line-height:31px}
.f-links li::before{content:"»";margin-right:22px}
.field{background:var(--white);color:#777;font-size:12px;padding:8px 16px}
.submit{left:699px;top:254px;width:144px;height:40px;background:var(--sky);font-size:13px;font-weight:700;display:flex;align-items:center;justify-content:center}
.f-rule{left:110px;top:344px;width:980px;height:1px;background:#333}
.f-social{left:110px;top:357px;display:flex;gap:7px}
.f-social span{width:28px;height:28px;border-radius:50%;background:var(--white)}
.copy{left:630px;top:362px;font-size:13px}
</style>
</head>
<body>

<header class="site-header">
  <div class="abs brand"><span class="brand-dot"></span>Sudsy Harbor Laundromat</div>
  <nav class="abs nav">
    <span>Home</span><span>About us</span><span>Services</span><span>Locations</span><span>Reviews</span><span>Contact us</span>
  </nav>
  <div class="abs call">
    <div class="abs call-icon">
      <svg width="22" height="22" viewBox="0 0 24 24"><path fill="#fff" d="M6.6 10.8a15.5 15.5 0 0 0 6.6 6.6l2.2-2.2c.3-.3.7-.4 1-.2 1.1.4 2.3.6 3.6.6.6 0 1 .4 1 1V20c0 .6-.4 1-1 1A17 17 0 0 1 3 4c0-.6.4-1 1-1h3.5c.6 0 1 .4 1 1 0 1.3.2 2.5.6 3.6.1.3 0 .7-.2 1z"/></svg>
    </div>
    <div class="abs call-label">Call us Today :</div>
    <div class="abs call-num">+1 800 555 0199</div>
  </div>
</header>

<section class="hero">
  <div class="hero-photo" role="img" aria-label="Photo of a woman in a blue dress walking between rows of washing machines in the laundromat"></div>
  <h1 class="abs hero-title">One of Atlanta's<br>first, finest, &amp;<br>friendliest<br>coin laundries</h1>
  <div class="abs btn-ghost">GET STARTED</div>
  <div class="abs dots"><span></span><span></span><span></span><span></span></div>
  <div class="abs social-side"><span style="background:var(--navy)"></span><span style="background:var(--sky)"></span><span style="background:#d9322b"></span></div>
</section>

<section class="about">
  <div class="abs about-photo-back" role="img" aria-label="Photo of the laundromat interior with rows of washers"></div>
  <div class="abs about-photo-front" role="img" aria-label="Photo of a woman in a blue dress seated in front of washing machines"></div>
  <div class="abs bubble" style="left:130px;top:332px;width:30px;height:30px"></div>
  <div class="abs bubble" style="left:199px;top:368px;width:22px;height:22px"></div>
  <div class="abs bubble" style="left:64px;top:410px;width:16px;height:16px;border-width:3px"></div>
  <div class="abs bubble" style="left:107px;top:428px;width:28px;height:28px;border-width:5px"></div>
  <div class="abs bubble" style="left:66px;top:452px;width:12px;height:12px;border-width:3px"></div>
  <div class="abs bubble" style="left:143px;top:468px;width:17px;height:17px;border-width:3px"></div>
  <div class="abs eyebrow">ABOUT US</div>
  <h2 class="abs about-title">SUDSY HARBOR</h2>
  <p class="abs about-text">Lorem ipsum dolor sit amet, consectetur adipiscing elit, sed do eiusmod tempor incididunt ut labore et dolore magna aliqua. Ut enim ad minim veniam, quis nostrud exercitat ion ullamco laboris nisi ut aliquip ex ea commodo conse quat. Duis aute irure dolor in reprehenderit in voluptate velit esse cillum dolore eu fugiat nulla pariatur. Excepteur sint occaecat cupidatat non proident, sunt in culpa qui officia deserunt mollit anim id est laborum.Lorem ipsum dolor sit amet, consectetur adipiscing elit, sed do eiusmod tempor incididunt ut labore et dolore magna aliqua. Ut enim ad minim veniam, quis nostrud exercitation ullamco laboris nisi ut aliquip ex ea commodo consequat. Duis aute irure dolor in reprehenderit in voluptate velit esse cillum dolore eu fugiat nulla pariatur. Excepteur sint occaecat cupidatat non proident, sunt in culpa qui officia deserunt mollit anim id est laborum.</p>
  <div class="abs btn-outline" style="left:651px;top:518px;width:155px;height:50px">LEARN MORE</div>
</section>

<section class="services">
  <h2 class="abs section-title" style="top:95px">SERVICES</h2>

  <article class="abs card" style="left:111px">
    <div class="card-photo" role="img" aria-label="Photo of a laundromat corner with washers and a vending machine" style="background:linear-gradient(135deg,#a7b6ad,#6d7b7a)"></div>
    <div class="card-icon"><svg width="40" height="40" viewBox="0 0 40 40" fill="none" stroke="#0677BA" stroke-width="2"><path d="M13 6l-8 5 3 7 4-2v18h16V16l4 2 3-7-8-5c-1 3-4 5-7 5s-6-2-7-5z"/></svg></div>
    <h3 class="card-title">Dry cleaning<br>drop off</h3>
    <div class="btn-solid">LEARN MORE <svg width="11" height="11" viewBox="0 0 12 12"><circle cx="6" cy="6" r="6" fill="#fff"/><path d="M5 3l3 3-3 3" stroke="#0054AA" stroke-width="2" fill="none"/></svg></div>
  </article>

  <article class="abs card" style="left:444px">
    <div class="card-photo" role="img" aria-label="Photo of folded white towels stacked in front of washers" style="background:linear-gradient(135deg,#dfe2e4,#8d9496)"></div>
    <div class="card-icon"><svg width="40" height="40" viewBox="0 0 40 40" fill="none" stroke="#0677BA" stroke-width="2"><rect x="8" y="5" width="24" height="30" rx="2"/><line x1="8" y1="11" x2="32" y2="11"/><circle cx="20" cy="23" r="8"/></svg></div>
    <h3 class="card-title">Professional laundry<br>services</h3>
    <div class="btn-solid">LEARN MORE <svg width="11" height="11" viewBox="0 0 12 12"><circle cx="6" cy="6" r="6" fill="#fff"/><path d="M5 3l3 3-3 3" stroke="#0054AA" stroke-width="2" fill="none"/></svg></div>
  </article>

  <article class="abs card" style="left:776px">
    <div class="card-photo" role="img" aria-label="Photo of a bright laundromat with folding tables and plants" style="background:linear-gradient(135deg,#c2cfc4,#7d8c86)"></div>
    <div class="card-icon"><svg width="40" height="40" viewBox="0 0 40 40" fill="none" stroke="#0677BA" stroke-width="2"><path d="M8 34V18l4-8 3 8M32 34V18l-4-8-3 8M15 18v-8M25 18v-8M20 16v-8"/></svg></div>
    <h3 class="card-title">Wash dry fold and self<br>service laundry</h3>
    <div class="btn-solid">LEARN MORE <svg width="11" height="11" viewBox="0 0 12 12"><circle cx="6" cy="6" r="6" fill="#fff"/><path d="M5 3l3 3-3 3" stroke="#0054AA" stroke-width="2" fill="none"/></svg></div>
  </article>
</section>

<section class="video">
  <svg class="abs" style="left:0;top:0" width="1200" height="440" viewBox="0 0 1200 440">
    <defs><linearGradient id="vg" x1="0" x2="1" y1="0" y2="0"><stop offset="0" stop-color="#0054AA"/><stop offset="1" stop-color="#1E9BD7"/></linearGradient></defs>
    <path d="M0 0H1200V278L0 440Z" fill="url(#vg)"/>
    <path d="M960 320L1200 278V410Z" fill="#CADEEF"/>
  </svg>
  <h2 class="abs section-title video-title">OUR VIDEO</h2>
  <p class="abs video-sub">Lorem ipsum dolor sit amet, consectetur adipiscing elit, sed do eiusmod tempor incididunt ut labore et dolore magna aliqua.</p>
  <div class="abs video-frame" role="img" aria-label="Video still of a man at the dry cleaning counter with garments on a rack">
    <div class="abs play"><svg width="26" height="28" viewBox="0 0 26 28"><path d="M3 2l21 12L3 26z" fill="#0677BA"/></svg></div>
  </div>
</section>

<section class="reviews">
  <h2 class="abs section-title" style="top:20px">REVIEWS</h2>
  <svg class="abs" style="left:38px;top:190px" width="28" height="40" viewBox="0 0 28 40"><path d="M22 4L6 20l16 16" stroke="#0054AA" stroke-width="6" fill="none"/></svg>
  <svg class="abs" style="left:1128px;top:190px" width="28" height="40" viewBox="0 0 28 40"><path d="M6 4l16 16L6 36" stroke="#0054AA" stroke-width="6" fill="none"/></svg>

  <div class="abs review" style="left:109px">
    <div class="stars">★★★★★</div>
    <p class="quote">"Lorem ipsum dolor sit amet, consectetur adipiscing elit, sed do eiusmod tempor incididunt ut labore et dolore magna aliqua. Ut enim ad minim veniam, quis nostrud rem ipsum dolor sit»</p>
    <svg class="tail" width="30" height="26" viewBox="0 0 30 26"><path d="M0 0L15 24L30 0" fill="#fff" stroke="#0677BA" stroke-width="2"/></svg>
  </div>
  <div class="abs review" style="left:441px">
    <div class="stars">★★★★★</div>
    <p class="quote">"Lorem ipsum dolor sit amet, consectetur adipiscing elit, sed do eiusmod tempor incididunt ut labore et dolore magna aliqua. Ut enim ad minim veniam, quis nostrud»</p>
    <svg class="tail" width="30" height="26" viewBox="0 0 30 26"><path d="M0 0L15 24L30 0" fill="#fff" stroke="#0677BA" stroke-width="2"/></svg>
  </div>
  <div class="abs review" style="left:774px">
    <div class="stars">★★★★★</div>
    <p class="quote">"Lorem ipsum dolor sit amet, consectetur adipiscing elit, sed do eiusmod tempor incididunt ut labore et dolore magna aliqua. Ut enim ad minim veniam, quis nostrud»</p>
    <svg class="tail" width="30" height="26" viewBox="0 0 30 26"><path d="M0 0L15 24L30 0" fill="#fff" stroke="#0677BA" stroke-width="2"/></svg>
  </div>

  <div class="abs reviewer" style="left:126px">John doe</div><div class="abs company" style="left:126px">Company name</div>
  <div class="abs reviewer" style="left:458px">John doe</div><div class="abs company" style="left:458px">Company name</div>
  <div class="abs reviewer" style="left:791px">John doe</div><div class="abs company" style="left:791px">Company name</div>
</section>

<section class="contact">
  <div class="abs map" role="img" aria-label="Street map showing the laundromat location and nearby shops"></div>
  <div class="abs contact-panel">
    <h2 class="abs contact-title">CONTACT US</h2>
    <div class="abs c-icon" style="top:136px"><svg width="16" height="20" viewBox="0 0 16 20"><path d="M8 0a7 7 0 0 0-7 7c0 5 7 13 7 13s7-8 7-13a7 7 0 0 0-7-7zm0 10a3 3 0 1 1 0-6 3 3 0 0 1 0 6z" fill="#0677BA"/></svg></div>
    <div class="abs c-text" style="top:126px">Address<br>Sudsy Harbor Atlanta - Maple Court Shopping Center, 2210 Birchwood Ave NE., # 118, Atlanta</div>
    <div class="abs c-icon" style="top:254px"><svg width="20" height="16" viewBox="0 0 20 16"><rect width="20" height="16" rx="2" fill="#0677BA"/><path d="M1 2l9 7 9-7" stroke="#fff" stroke-width="2" fill="none"/></svg></div>
    <div class="abs c-text" style="top:252px">Email<br>info@sudsyharbor.example</div>
    <div class="abs c-icon" style="top:348px"><svg width="18" height="18" viewBox="0 0 24 24"><path fill="#0677BA" d="M6.6 10.8a15.5 15.5 0 0 0 6.6 6.6l2.2-2.2c.3-.3.7-.4 1-.2 1.1.4 2.3.6 3.6.6.6 0 1 .4 1 1V20c0 .6-.4 1-1 1A17 17 0 0 1 3 4c0-.6.4-1 1-1h3.5c.6 0 1 .4 1 1 0 1.3.2 2.5.6 3.6.1.3 0 .7-.2 1z"/></svg></div>
    <div class="abs c-text" style="top:346px">Phone<br>(404) 555-0142</div>
    <div class="abs ring" style="left:436px;top:278px;width:26px;height:26px"></div>
    <div class="abs ring" style="left:504px;top:306px;width:16px;height:16px;border-width:3px"></div>
    <div class="abs ring" style="left:410px;top:362px;width:28px;height:28px;border-width:5px"></div>
    <div class="abs ring" style="left:368px;top:352px;width:14px;height:14px;border-width:3px"></div>
    <div class="abs ring" style="left:447px;top:402px;width:16px;height:16px;border-width:3px"></div>
  </div>
</section>

<footer class="site-footer">
  <div class="abs f-head" style="left:113px">GET IN TOUCH</div>
  <div class="abs f-line" style="left:113px;top:94px"></div>
  <div class="abs f-row" style="top:116px"><span class="f-ico"><svg width="10" height="13" viewBox="0 0 16 20"><path d="M8 0a7 7 0 0 0-7 7c0 5 7 13 7 13s7-8 7-13a7 7 0 0 0-7-7z" fill="#fff"/></svg></span><span>Maple Court Shopping Center, 2210<br>Birchwood Ave NE., # 118, Atlanta,<br>GA 30300</span></div>
  <div class="abs f-row" style="top:196px;align-items:center"><span class="f-ico"><svg width="12" height="12" viewBox="0 0 24 24"><path fill="#fff" d="M6.6 10.8a15.5 15.5 0 0 0 6.6 6.6l2.2-2.2c.3-.3.7-.4 1-.2 1.1.4 2.3.6 3.6.6.6 0 1 .4 1 1V20c0 .6-.4 1-1 1A17 17 0 0 1 3 4c0-.6.4-1 1-1h3.5c.6 0 1 .4 1 1 0 1.3.2 2.5.6 3.6.1.3 0 .7-.2 1z"/></svg></span><span>(404) 555-0142</span></div>
  <div class="abs f-row" style="top:250px;align-items:center"><span class="f-ico"><svg width="12" height="10" viewBox="0 0 20 16"><rect width="20" height="16" rx="2" fill="#fff"/></svg></span><span>info@sudsyharbor.example</span></div>

  <div class="abs f-head" style="left:465px">INFORMATION</div>
  <div class="abs f-line" style="left:465px;top:94px"></div>
  <ul class="abs f-links"><li>Home Page</li><li>About us</li><li>Privacy Policy</li><li>Support</li><li>Contact us</li></ul>

  <div class="abs f-head" style="left:699px">CONTACT US</div>
  <div class="abs f-line" style="left:699px;top:94px"></div>
  <div class="abs field" style="left:699px;top:108px;width:190px;height:32px">Name</div>
  <div class="abs field" style="left:898px;top:108px;width:190px;height:32px">Email Address</div>
  <div class="abs field" style="left:699px;top:150px;width:389px;height:80px">Message</div>
  <div class="abs submit">SUBMIT MESSAGE</div>

  <div class="abs f-rule"></div>
  <div class="abs f-social"><span></span><span></span><span></span></div>
  <div class="abs copy">© Copyrights 2021 Company name | All Rights Reserved | Privacy Policy</div>
</footer>

</body>
</html>
```